Lorna Tess Tresses Fancy Business Card’s

I want my business cards to be elite, original and very classy. I want the business cards to match the colors of my logo and to match the design posted. I would love the design of the picture I posted

I want the card all white .
The dripping on the top of the card I want it to match the pink color in my logo that’s also posted .
I need my logo on the business card !
I need my Instagram- @lorna.tess.tresses__
And my phone number - 582 907 3365

Target Market(s)

My target market is young woman age 23 to older woman to the age of 65
I want both older and younger women to love my design . I don’t want any cheap looking business cards

Industry/Entity Type

Hair And Beauty

Contact Information for Business Card

Add my logo
Add my Instagram- @lorna.tess.tresses__
My number - 582 907 3365
My website- www.lornatesstresses.example

Font styles to use
Serif
Script

Colors
ffffff
e667a6
e34298

Requirements
Must have
• The business cards must have my logo, my number , my website, and my Instagram!
Nice to have
• Nice to have glitter words that match my logo
• The business cards must look classy and mature
• I want them to be very unique!!
Should not have
• Should not have any colors that doesn’t match my logo ! This is very important! Please

```html
<!DOCTYPE html>
<html lang="en">
<head>
<meta charset="utf-8">
<title>Lorna Tess Tresses – Business Card</title>
<link href="https://fonts.googleapis.com/css2?family=Courgette&family=Great+Vibes&display=swap" rel="stylesheet">
<style>
  :root {
    --page: #fdfdfd;
    --card: #e7e8ea;
    --pink: #e5479b;
    --ink: #111111;
    --rule: #7a7a76;
  }
  html, body {
    margin: 0;
    width: 1200px;
    height: 900px;
    overflow: hidden;
    background: var(--page);
  }
  .canvas {
    position: relative;
    width: 1200px;
    height: 900px;
  }
  .card {
    position: absolute;
    left: 233px;
    top: 255px;
    width: 761px;
    height: 435px;
    background: var(--card);
    border-radius: 33px;
  }
  .band {
    position: absolute;
    left: 57px;
    width: 647px;
    height: 17px;
    background: var(--pink);
  }
  .band--top { top: 0; }
  .band--bottom { bottom: 0; }
  .brand {
    position: absolute;
    left: 110px;
    top: 150px;
    width: 160px;
    margin: 0;
    font-family: "Great Vibes", cursive;
    font-weight: 400;
    font-size: 46px;
    line-height: 0.95;
    color: var(--pink);
    text-align: center;
  }
  .divider {
    position: absolute;
    left: 335px;
    top: 130px;
    width: 2px;
    height: 176px;
    background: var(--rule);
  }
  .contacts {
    position: absolute;
    left: 398px;
    top: 164px;
    margin: 0;
    padding: 0;
    list-style: none;
  }
  .contact {
    display: flex;
    align-items: center;
    height: 30px;
    margin-bottom: 8.5px;
    font-family: "Courgette", cursive;
    font-size: 21px;
    color: var(--ink);
    white-space: nowrap;
  }
  .contact__icon {
    width: 30px;
    height: 30px;
    margin-right: 11px;
    flex: none;
  }
</style>
</head>
<body>
<div class="canvas">
  <div class="card">
    <div class="band band--top"></div>

    <p class="brand">Lorna Tess Tresses</p>

    <div class="divider"></div>

    <ul class="contacts">
      <li class="contact">
        <svg class="contact__icon" viewBox="0 0 30 30" aria-hidden="true">
          <circle cx="15" cy="15" r="13.5" fill="none" stroke="#111" stroke-width="1.5"/>
          <rect x="10" y="7" width="10" height="17" rx="2" fill="#111"/>
          <rect x="11.5" y="10" width="7" height="4.5" fill="#e7e8ea"/>
          <circle cx="15" cy="20" r="1" fill="#e7e8ea"/>
          <rect x="10.5" y="4.5" width="1.4" height="3" fill="#111"/>
        </svg>
        <span class="contact__text">582 907 3365</span>
      </li>
      <li class="contact">
        <svg class="contact__icon" viewBox="0 0 30 30" aria-hidden="true">
          <circle cx="15" cy="15" r="13.5" fill="none" stroke="#111" stroke-width="1.5"/>
          <circle cx="15" cy="15" r="6" fill="#111"/>
        </svg>
        <span class="contact__text">@lorna.tess.tresses__</span>
      </li>
      <li class="contact">
        <svg class="contact__icon" viewBox="0 0 30 30" aria-hidden="true">
          <circle cx="15" cy="15" r="13.5" fill="none" stroke="#111" stroke-width="1.5"/>
          <circle cx="15" cy="15" r="8.5" fill="#111"/>
          <g fill="none" stroke="#e7e8ea" stroke-width="0.9">
            <ellipse cx="15" cy="15" rx="3.5" ry="8.5"/>
            <line x1="15" y1="6.5" x2="15" y2="23.5"/>
            <line x1="6.5" y1="15" x2="23.5" y2="15"/>
            <line x1="8" y1="10.5" x2="22" y2="10.5"/>
            <line x1="8" y1="19.5" x2="22" y2="19.5"/>
          </g>
        </svg>
        <span class="contact__text">www.lornatesstresses.example</span>
      </li>
    </ul>

    <div class="band band--bottom"></div>
  </div>
</div>
</body>
</html>
```